Namecard Designs+Logo for a High End Automobile Company

We need a new business card for our company called Velta Motorhof.

www.veltamotorhof.example.sg
Our new website will be up in 2.5 months time.

We sell used and brand new continental cars like Korvane, QTL, Dravell, Solbrini and etc. Currently we are operating from 2 offices in Singapore and United Kingdom.

We want a design which is serious. We are open to colours but try to keep it at a maximum of 3 colours.

We prefer something simple and minimal. We are open to 2 sides printing or even 2 sided namecards. Both UK and Singapore company offices address must be in; either side by side, front and back, or even 2 sided cards.

The logo can be a text logo, emblem, abstract, pictorial or combination.

We are printing with Pribo.com so please kindly follow the printing guideline.

http://uk.pribo.example/help/faq/templates-and-guidelines.html

Rich and Car Enthusiasts

Printing

Must have
• Our 2 offices; UK and Singapore.

Our slogan which is " The Automobile Specialist"
Should not have
• Not more than 3 colours

```html
<!DOCTYPE html>
<html lang="en">
<head>
<meta charset="utf-8">
<title>Velta Motorhof – business card</title>
<link rel="stylesheet" href="https://fonts.googleapis.com/css2?family=Poiret+One&display=swap">
<style>
  :root {
    --stage: #c9c9c9;
    --card: #ffffff;
    --red: #9b1b1e;
    --grey: #6f6f6f;
    --light: #a8a8a8;
    --ink: #2a2a2a;
    --band: #9e9e9e;
  }
  * { margin: 0; padding: 0; box-sizing: border-box; }
  html, body { width: 1200px; height: 900px; overflow: hidden; }
  body {
    background: var(--stage);
    font-family: "Poiret One", sans-serif;
    position: relative;
  }
  .card {
    position: absolute;
    width: 640px;
    height: 400px;
    background: var(--card);
    overflow: hidden;
  }
  .card--front { left: 40px; top: 40px; }
  .card--back  { left: 520px; top: 460px; }

  .band {
    position: absolute;
    background: var(--band);
    height: 40px;
  }

  /* front */
  .brand {
    position: absolute;
    left: 26px;
    top: 190px;
    width: 186px;
  }
  .brand__name {
    font-size: 25px;
    color: var(--ink);
    line-height: 1;
    white-space: nowrap;
  }
  .brand__slogan {
    font-size: 12px;
    color: var(--light);
    margin-top: 6px;
    white-space: nowrap;
  }
  .card--front .band { left: 222px; right: 0; top: 188px; }

  /* back */
  .person {
    position: absolute;
    left: 0; right: 60px;
    top: 62px;
    text-align: center;
  }
  .person__name {
    font-size: 50px;
    color: var(--red);
    line-height: 1;
  }
  .person__role {
    font-size: 30px;
    color: var(--ink);
    margin-top: 4px;
    line-height: 1;
  }
  .card--back .band { left: 0; right: 0; top: 180px; }

  .contact {
    position: absolute;
    left: 16px;
    top: 282px;
    font-size: 18px;
    color: var(--grey);
    line-height: 22px;
    display: grid;
    grid-template-columns: 62px 18px auto;
    white-space: nowrap;
  }
  .contact .at { color: var(--red); }

  .offices {
    position: absolute;
    left: 428px;
    top: 238px;
    bottom: 0;
    border-left: 3px solid var(--red);
    padding: 6px 0 0 16px;
    font-size: 14px;
    color: var(--grey);
    line-height: 17px;
    white-space: nowrap;
  }
  .office + .office { margin-top: 26px; }
  .office__country { color: var(--red); }
</style>
</head>
<body>

  <section class="card card--front" aria-label="Card front">
    <div class="brand">
      <div class="brand__name">Velta Motorhof</div>
      <div class="brand__slogan">The Automobile Specialist</div>
    </div>
    <div class="band" role="img" aria-label="Grey checkered band"></div>
  </section>

  <section class="card card--back" aria-label="Card back">
    <div class="person">
      <div class="person__name">lena corvick</div>
      <div class="person__role">designer</div>
    </div>
    <div class="band" role="img" aria-label="Grey checkered band"></div>

    <div class="contact">
      <span>email</span><span>:</span><span>lena<span class="at">@</span>veltamotorhof.example.sg</span>
      <span>tel</span><span>:</span><span>+65-8-5550-0142</span>
      <span>web</span><span>:</span><span>http://veltamotorhof.example.sg</span>
    </div>

    <div class="offices">
      <div class="office">
        <div>suite 14, 210 marlow st.</div>
        <div>alderby, nw 2140</div>
        <div class="office__country">united kingdom</div>
      </div>
      <div class="office">
        <div>suite 8, 52 tanvale rd.</div>
        <div>keswin, 048211</div>
        <div class="office__country">singapore</div>
      </div>
    </div>
  </section>

</body>
</html>
```